Top notch designer needed for world class recruitment app!

We need an app design for an Amsterdam-based company that is about to change the way we find new jobs. The idea is not to show the company and job title as everyone does, but only a 5 sentence summary of the job. The user slides though the jobs and eventuelly finds a shortlist of his best matching jobs.

Winning designers supplies 2 designs, that have contain the core of our business idea (see screenshots attached):

Screenshot 1, A job description done in 5 bulletpoints (6-9 words).

example:

- Lead 20 enthusiastic workers
- Coordinate between production department and development team
- Improve current processes
- Maintain relations with supplier
- Lot of focus on personal development

Screenshot 2 should be a shortlist/favourites

The shortlists shows around 5 jobs with job title, company logo, number of days the
vacancy will stay available, and how well the job matches to your profile (preferably by means of a visual indicator).

Target Market(s)

Young professionals looking for a job. Well educated withless than 10 years work experience. Typical user would be someone who uses staffwell regularly.

Industry/Entity Type

Business

Requirements
Must have
• The 2 screenshots (see attachment) with awesome look and feel, with content as described in attachment.. The winning designs should (also) be available in PSD format, or less preferably in PNG.

Nice to have
• Inspiration:
Swoopa: simple and clear slide throughs (yes/no)
Staffwell: start screen (professional and stylish), vacancy banner (visual, but not distracting)
Roomvex: combination of playfull and professional design
Should not have
• We like to have it as visual as possible, but visuals cannot directly relate to the job (because we cannot match a visual to every job). So should be something 'business like' or 'city life'.

When a user clicks on the 'i (more info)' button the user can see info like job title, company name, location. Its important that this info is not shown in screenshot 1.

```html
<!DOCTYPE html>
<html lang="en">
<head>
<meta charset="utf-8">
<title>Jobvela – recruitment app screens</title>
<link href="https://fonts.googleapis.com/css2?family=Montserrat:wght@400;500;600;700&family=Open+Sans:wght@400;600;700&display=swap" rel="stylesheet">
<style>
  :root {
    --red: #e0303c;
    --red-soft: #ec5a63;
    --red-deep: #c9202c;
    --ink: #3a3a3a;
    --muted: #8a8a8a;
    --line: #e6e6e6;
    --paper: #ffffff;
    --stage: #eceff0;
    --stage-edge: #dfe3e4;
    --green: #58c13a;
    --amber: #f5b021;
  }
  * { box-sizing: border-box; margin: 0; padding: 0; }
  html, body { width: 1200px; height: 777px; overflow: hidden; }
  body {
    background: radial-gradient(ellipse at 50% 40%, var(--stage) 0%, var(--stage-edge) 100%);
    font-family: "Open Sans", Arial, sans-serif;
    color: var(--ink);
    position: relative;
  }
  .screen {
    position: absolute;
    top: 180px;
    width: 260px;
    height: 410px;
    background: var(--paper);
    overflow: hidden;
    box-shadow: 0 10px 30px rgba(0,0,0,.12);
  }
  .screen--card { left: 150px; }
  .screen--start { left: 470px; }
  .screen--shortlist { left: 790px; }

  /* shared app bar */
  .app-bar {
    height: 44px;
    display: flex;
    align-items: center;
    justify-content: center;
    position: relative;
    border-bottom: 1px solid var(--line);
    background: var(--paper);
  }
  .menu-icon { position: absolute; left: 12px; top: 16px; }
  .app-title {
    color: var(--red);
    font-family: "Montserrat", sans-serif;
    font-weight: 600;
    font-size: 15px;
  }
  .avatar {
    position: absolute;
    right: 8px; top: 8px;
    width: 26px; height: 26px;
    border-radius: 4px;
    background: linear-gradient(160deg, #c9b6a6, #7d6a5c);
  }

  /* job card screen */
  .screen--card { background: #f3f3f3; }
  .job-card {
    position: absolute;
    left: 14px; right: 14px; top: 58px;
    height: 240px;
    background: var(--paper);
    border-radius: 4px;
    box-shadow: 0 1px 3px rgba(0,0,0,.15), 0 4px 0 -1px #fafafa, 0 5px 2px -1px rgba(0,0,0,.12), 0 9px 0 -2px #fafafa, 0 10px 2px -2px rgba(0,0,0,.1);
  }
  .job-banner {
    height: 58px;
    background: linear-gradient(90deg, var(--red-soft), var(--red));
    border-radius: 4px 4px 0 0;
    position: relative;
  }
  .banner-photo {
    position: absolute;
    left: 50%; top: 6px;
    width: 38px; height: 38px;
    margin-left: -19px;
    border-radius: 50%;
    border: 2px solid var(--paper);
    background: linear-gradient(160deg, #9aa3ab, #5d666e);
  }
  .job-points { list-style: none; padding: 14px 14px 0 14px; }
  .job-points li {
    font-size: 11.5px;
    line-height: 1.35;
    margin-bottom: 10px;
    padding-left: 8px;
    position: relative;
  }
  .job-points li::before { content: "•"; position: absolute; left: 0; }
  .card-actions {
    position: absolute;
    left: 0; right: 0; bottom: 0;
    height: 82px;
    background: var(--paper);
    border-top: 1px solid var(--line);
    display: flex;
    justify-content: center;
    align-items: center;
    gap: 18px;
  }

  /* start screen */
  .screen--start {
    background: linear-gradient(170deg, #e85763 0%, var(--red) 50%, var(--red-deep) 100%);
    color: var(--paper);
    text-align: center;
  }
  .start-visual {
    position: absolute; inset: 0;
    background: radial-gradient(ellipse at 40% 35%, rgba(255,255,255,.14), rgba(255,255,255,0) 60%);
  }
  .brand {
    position: absolute; left: 0; right: 0; top: 138px;
    text-align: center;
  }
  .brand-name {
    font-family: "Montserrat", sans-serif;
    font-weight: 600;
    font-size: 34px;
    letter-spacing: .5px;
  }
  .tagline {
    position: absolute; left: 0; right: 0; top: 196px;
    font-family: "Montserrat", sans-serif;
    font-size: 11.5px;
    letter-spacing: 1.6px;
    line-height: 1.4;
  }
  .start-actions {
    position: absolute; left: 14px; right: 14px; bottom: 24px;
    display: flex; gap: 6px;
  }
  .start-actions span {
    flex: 1;
    border: 1px solid rgba(255,255,255,.85);
    padding: 11px 0;
    font-family: "Montserrat", sans-serif;
    font-size: 13px;
  }

  /* shortlist */
  .shortlist { list-style: none; }
  .shortlist li {
    height: 73px;
    border-bottom: 1px solid var(--line);
    display: flex;
    align-items: center;
    padding: 0 8px 0 8px;
    position: relative;
  }
  .company-mark {
    width: 30px; height: 30px;
    border-radius: 50%;
    border: 1px solid var(--line);
    flex: none;
    margin-right: 6px;
  }
  .job-info { flex: 1; min-width: 0; }
  .company {
    font-family: "Open Sans", sans-serif;
    font-weight: 700;
    font-size: 11.5px;
    color: var(--ink);
  }
  .role { font-size: 8.5px; color: var(--muted); line-height: 1.3; margin-top: 2px; }
  .meta { width: 34px; text-align: center; flex: none; }
  .days { font-size: 9px; line-height: 1; color: var(--ink); }
  .days small { display: block; font-size: 6.5px; line-height: 1.1; }
  .match {
    width: 22px; height: 22px; border-radius: 50%;
    margin: 3px auto 0;
    color: var(--paper);
    font-size: 7.5px; font-weight: 700;
    display: flex; flex-direction: column; align-items: center; justify-content: center;
    line-height: 1;
  }
  .match small { font-size: 4.5px; font-weight: 400; }
  .match--high { background: var(--green); }
  .match--mid { background: var(--amber); }
  .match--low { background: var(--red); }
  .chevron { margin-left: 6px; flex: none; }
</style>
</head>
<body>

<section class="screen screen--card" aria-label="Job card">
  <header class="app-bar">
    <svg class="menu-icon" width="16" height="12" viewBox="0 0 16 12"><path d="M0 1h16M0 6h16M0 11h16" stroke="#e0303c" stroke-width="1.6"/></svg>
    <span class="app-title">Jobvela</span>
    <span class="avatar" role="img" aria-label="User profile photo"></span>
  </header>
  <article class="job-card">
    <div class="job-banner" role="img" aria-label="City life banner">
      <span class="banner-photo" role="img" aria-label="City building photo"></span>
    </div>
    <ul class="job-points">
      <li>Lead 20 enthusiastic workers</li>
      <li>Coordinate between production department and development team</li>
      <li>Improve current processes</li>
      <li>Maintain relations with supplier</li>
      <li>Lot of focus on personal development</li>
    </ul>
  </article>
  <nav class="card-actions">
    <svg width="38" height="38" viewBox="0 0 38 38" aria-label="Dislike"><circle cx="19" cy="19" r="17" fill="none" stroke="#e0303c" stroke-width="1.4"/><path d="M12 12h10l3 8h-6l1 6-3 1-5-8z M12 12v8" fill="none" stroke="#e0303c" stroke-width="1.4" stroke-linejoin="round"/></svg>
    <svg width="38" height="38" viewBox="0 0 38 38" aria-label="More info"><circle cx="19" cy="19" r="17" fill="none" stroke="#e0303c" stroke-width="1.4"/><circle cx="19" cy="12" r="1.6" fill="#e0303c"/><path d="M19 16v11" stroke="#e0303c" stroke-width="2.4"/></svg>
    <svg width="38" height="38" viewBox="0 0 38 38" aria-label="Like"><circle cx="19" cy="19" r="17" fill="none" stroke="#e0303c" stroke-width="1.4"/><path d="M12 26h10l3-8h-6l1-6-3-1-5 8z M12 26v-8" fill="none" stroke="#e0303c" stroke-width="1.4" stroke-linejoin="round"/></svg>
  </nav>
</section>

<section class="screen screen--start" aria-label="Start screen">
  <div class="start-visual" role="img" aria-label="Faded business city scene"></div>
  <div class="brand"><span class="brand-name">Jobvela</span></div>
  <p class="tagline">The world's best<br>recruitment network</p>
  <div class="start-actions"><span>Join Now</span><span>Sign in</span></div>
</section>

<section class="screen screen--shortlist" aria-label="Shortlist">
  <header class="app-bar">
    <svg class="menu-icon" width="16" height="12" viewBox="0 0 16 12"><path d="M0 1h16M0 6h16M0 11h16" stroke="#e0303c" stroke-width="1.6"/></svg>
    <span class="app-title">Shortlist</span>
    <span class="avatar" role="img" aria-label="User profile photo"></span>
  </header>
  <ul class="shortlist">
    <li><span class="company-mark"></span><div class="job-info"><div class="company">Brouwmark</div><div class="role">Coordinator Products &amp; Technics</div></div><div class="meta"><div class="days">15<small>Days Left</small></div><div class="match match--high">75%<small>match</small></div></div><svg class="chevron" width="7" height="16" viewBox="0 0 7 16"><path d="M1 1l5 7-5 7" fill="none" stroke="#e0303c" stroke-width="1.2"/></svg></li>
    <li><span class="company-mark"></span><div class="job-info"><div class="company">Lumora</div><div class="role">Global Acceptance Manager</div></div><div class="meta"><div class="days">8<small>Days Left</small></div><div class="match match--mid">60%<small>match</small></div></div><svg class="chevron" width="7" height="16" viewBox="0 0 7 16"><path d="M1 1l5 7-5 7" fill="none" stroke="#e0303c" stroke-width="1.2"/></svg></li>
    <li><span class="company-mark"></span><div class="job-info"><div class="company">Verdaal</div><div class="role">Financial Reporter</div></div><div class="meta"><div class="days">0<small>Days Left</small></div><div class="match match--mid">60%<small>match</small></div></div><svg class="chevron" width="7" height="16" viewBox="0 0 7 16"><path d="M1 1l5 7-5 7" fill="none" stroke="#e0303c" stroke-width="1.2"/></svg></li>
    <li><span class="company-mark"></span><div class="job-info"><div class="company">Cellora</div><div class="role">Project Manager New Business</div></div><div class="meta"><div class="days">8<small>Days Left</small></div><div class="match match--low">40%<small>match</small></div></div><svg class="chevron" width="7" height="16" viewBox="0 0 7 16"><path d="M1 1l5 7-5 7" fill="none" stroke="#e0303c" stroke-width="1.2"/></svg></li>
    <li><span class="company-mark"></span><div class="job-info"><div class="company">Lithex</div><div class="role">SCM Project Manager</div></div><div class="meta"><div class="days">24<small>Days Left</small></div><div class="match match--low">0%<small>match</small></div></div><svg class="chevron" width="7" height="16" viewBox="0 0 7 16"><path d="M1 1l5 7-5 7" fill="none" stroke="#e0303c" stroke-width="1.2"/></svg></li>
  </ul>
</section>

</body>
</html>
```